Verpackung für Feinkost
Vielen Dank! Tolle professionelle Zusammenarbeit. Selbst komplizierte, detaillierte und umfangreiche Anmerkdungen und Änderungswünsche werden genau gelesen und umgesetzt. Das Ergebnis ist erstklassig!
Zielgruppe
Wir sind ein junges Unternehmen und bauen aktuell einen Onlineshop auf, in dem wir hochwertige Geschenkboxen verkaufen möchten, die Feinkost und Lesegenuss miteinander kombinieren. Wir verkaufen nicht nur Feinkost in einer Box, sondern ein kulinarisches Abenteuer. Unsere Hauptzielgruppe sind literaturaffine Frauen im Alter zwischen 30 und 60 Jahren.
Aufgabenstellung
Wir haben bereits einen groben Designentwurf, der professionell umgesetzt werden soll (siehe Briefing-PDF). Lizenzen für unser Logo-Icon und die Schriftarten sind vorhanden. Eine Druckvorlage (Aufriss) vom Verpackungshersteller ist ebenfalls vorhanden und müsste dann befüllt werden (siehe Dateien).

```html
<!DOCTYPE html>
<html lang="de">
<head>
<meta charset="utf-8">
<title>Lesetruhe – Verpackungsaufriss</title>
<link rel="stylesheet" href="https://fonts.googleapis.com/css2?family=Cormorant+Garamond:wght@600&family=Great+Vibes&display=swap">
<style>
  :root {
    --paper: #ffffff;
    --night: #1c1660;
    --cut: #e0198c;
    --glue: #1f9a5a;
    --fold: #d9a07a;
    --gold: #c9953a;
    --violet: #4a3fa6;
    --lavender: #8a86c8;
    --peach: #f2a77c;
  }
  html, body {
    margin: 0;
    width: 1200px;
    height: 1177px;
    overflow: hidden;
    background: var(--paper);
  }
  .dieline {
    position: relative;
    width: 1200px;
    height: 1177px;
  }
  .dieline svg { position: absolute; inset: 0; }
  .brand-name {
    position: absolute;
    left: 380px; width: 439px;
    top: 550px;
    margin: 0;
    text-align: center;
    font-family: "Cormorant Garamond", serif;
    font-weight: 600;
    font-size: 46px;
    line-height: 1;
    color: var(--gold);
  }
  .theme-line {
    position: absolute;
    left: 380px; width: 439px;
    top: 622px;
    margin: 0;
    text-align: center;
    font-family: "Great Vibes", cursive;
    font-size: 24px;
    line-height: 1;
    color: var(--gold);
  }
</style>
</head>
<body>
<main class="dieline">
  <svg width="1200" height="1177" viewBox="0 0 1200 1177">
    <!-- glue tabs -->
    <g class="glue-tabs" fill="none" stroke="var(--glue)" stroke-width="1">
      <path d="M384 131 V73 H816 V131"/>
      <path d="M384 1038 V1095 H816 V1038"/>
      <path d="M147 365 H89 V804 H147"/>
      <path d="M1053 365 H1111 V804 H1053"/>
      <path d="M143 365 L152 358 L156 326 H374 V360 L380 365"/>
      <path d="M143 804 L152 811 L156 843 H374 V809 L380 804"/>
      <path d="M1057 365 L1048 358 L1044 326 H826 V360 L819 365"/>
      <path d="M1057 804 L1048 811 L1044 843 H826 V809 L819 804"/>
    </g>
    <!-- printed panels -->
    <g class="panels" fill="var(--night)" stroke="var(--cut)" stroke-width="1">
      <path d="M380 131 H819 V365 H1053 V804 H819 V1038 H380 V804 H147 V365 H380 Z"/>
    </g>
    <rect class="lid-fold" x="380" y="365" width="439" height="439" fill="none" stroke="var(--fold)" stroke-width="0.8"/>

    <!-- gold corner frames -->
    <g class="corner-frames" fill="none" stroke="var(--gold)" stroke-width="1.2">
      <path d="M677 385 H798 V506"/>
      <path d="M684 390 H793 V501"/>
      <path d="M401 662 V783 H523"/>
      <path d="M406 667 V778 H518"/>
    </g>

    <!-- floral illustrations -->
    <g role="img" aria-label="Illustration: Monstera-Blätter in Lavendel">
      <ellipse cx="410" cy="388" rx="28" ry="34" fill="var(--lavender)"/>
      <ellipse cx="455" cy="376" rx="32" ry="37" fill="var(--lavender)"/>
    </g>
    <g role="img" aria-label="Illustration: Zweig mit pfirsichfarbenen Blättern">
      <ellipse cx="398" cy="418" rx="50" ry="28" fill="var(--peach)" transform="rotate(35 398 418)"/>
    </g>
    <g role="img" aria-label="Illustration: violette Blüte">
      <circle cx="640" cy="368" r="27" fill="var(--violet)"/>
    </g>
    <g role="img" aria-label="Illustration: violette Blüte mit Monstera-Blatt im Rahmen">
      <rect x="705" y="401" width="77" height="86" fill="var(--peach)" opacity="0.9"/>
      <circle cx="730" cy="430" r="40" fill="var(--violet)"/>
    </g>
    <g role="img" aria-label="Illustration: violette Blüte">
      <circle cx="388" cy="598" r="44" fill="var(--violet)"/>
    </g>
    <g role="img" aria-label="Illustration: Monstera-Blatt und Pfirsichzweig im Rahmen">
      <rect x="416" y="677" width="48" height="89" fill="var(--lavender)"/>
      <ellipse cx="476" cy="740" rx="30" ry="28" fill="var(--peach)"/>
    </g>
    <g role="img" aria-label="Illustration: violette Blüte">
      <circle cx="592" cy="785" r="43" fill="var(--violet)"/>
    </g>
    <g role="img" aria-label="Illustration: Zweig mit lavendelfarbenen Blättern">
      <ellipse cx="790" cy="785" rx="36" ry="78" fill="var(--lavender)" opacity="0.85" transform="rotate(-20 790 785)"/>
    </g>
    <g class="small-blossoms" role="img" aria-label="Illustration: kleine Streublüten">
      <circle cx="479" cy="288" r="7" fill="var(--peach)"/>
      <circle cx="448" cy="310" r="5" fill="var(--violet)"/>
      <circle cx="543" cy="385" r="7" fill="var(--peach)"/>
      <circle cx="506" cy="405" r="14" fill="var(--violet)"/>
      <circle cx="525" cy="429" r="5" fill="var(--violet)"/>
      <circle cx="717" cy="325" r="11" fill="var(--violet)"/>
      <circle cx="741" cy="338" r="5" fill="var(--peach)"/>
      <circle cx="402" cy="480" r="12" fill="var(--violet)"/>
      <circle cx="427" cy="547" r="7" fill="var(--peach)"/>
      <circle cx="333" cy="660" r="5" fill="var(--violet)"/>
      <circle cx="352" cy="689" r="7" fill="var(--peach)"/>
      <circle cx="858" cy="481" r="7" fill="var(--peach)"/>
      <circle cx="889" cy="460" r="5" fill="var(--violet)"/>
      <circle cx="820" cy="542" r="14" fill="var(--violet)"/>
      <circle cx="728" cy="492" r="5" fill="var(--violet)"/>
      <circle cx="765" cy="689" r="11" fill="var(--peach)"/>
      <circle cx="714" cy="753" r="14" fill="var(--violet)"/>
      <circle cx="684" cy="770" r="7" fill="var(--peach)"/>
      <circle cx="701" cy="782" r="5" fill="var(--violet)"/>
      <circle cx="852" cy="743" r="5" fill="var(--violet)"/>
      <circle cx="757" cy="827" r="5" fill="var(--peach)"/>
      <circle cx="496" cy="836" r="15" fill="var(--violet)"/>
      <circle cx="453" cy="829" r="5" fill="var(--violet)"/>
      <circle cx="541" cy="869" r="7" fill="var(--peach)"/>
    </g>

    <circle class="brand-dot" cx="599" cy="523" r="16" fill="var(--gold)"/>
  </svg>

  <h1 class="brand-name">Lesetruhe</h1>
  <p class="theme-line">Tausendundeine Nacht</p>
</main>
</body>
</html>
```